Website visual upgrade

I am seeking expressions of interest for the updating the visuals of my website www.lunvaleplacements.example
I am basically seeking a simple,bold and visually strong graphic makeover.using existing or shortly to be modified text.

```html
<!DOCTYPE html>
<html lang="en">
<head>
<meta charset="utf-8">
<title>Lunvale Placements</title>
<link href="https://fonts.googleapis.com/css2?family=Oswald:wght@400;500&family=Roboto+Condensed:wght@300;400;700&family=Roboto:wght@500;700&family=Open+Sans:wght@400&display=swap" rel="stylesheet">
<style>
:root{
  --red:#c41230;
  --red-dark:#a0122b;
  --ink:#3c3c3c;
  --grey:#555;
  --line:#d9d9d9;
  --row:#f2f2f2;
  --panel:#f8f8f8;
  --social:#6b6b6b;
}
*{margin:0;padding:0;box-sizing:border-box}
html,body{width:1193px;height:1200px;overflow:hidden;background:#fff}
.page{position:relative;width:1193px;height:1200px;font-family:"Roboto Condensed",sans-serif;color:var(--ink)}
.abs{position:absolute}

/* header */
.brand{left:68px;top:30px;display:flex;align-items:center;gap:12px}
.brand-mark{width:26px;height:26px;background:#222;border-radius:50%}
.brand-name{font-family:"Roboto Condensed",sans-serif;font-weight:700;font-size:31px;color:var(--red);letter-spacing:.5px;line-height:1}
.nav-home{left:412px;top:0;width:68px;height:86px;background:#f3f3f3;border-bottom:4px solid var(--red)}
.nav a{position:absolute;top:48px;font-weight:300;font-size:14.5px;color:#444;text-decoration:none;white-space:nowrap}
.header-rule{left:68px;top:86px;width:1059px;height:1px;background:var(--line)}

/* band */
.band{left:0;top:103px;width:1193px;height:30px;background:var(--red)}
.social{right:67px;top:0;display:flex;gap:2px}
.social span{display:block;width:30px;height:30px;background:var(--social)}

/* hero */
.hero-map{left:0;top:133px;width:760px;height:328px;background:linear-gradient(135deg,#ffffff 0%,#f2f5f8 55%,#e6edf3 100%)}
.hero-photo{left:760px;top:133px;width:433px;height:328px;background:linear-gradient(90deg,#f3f3f3 0%,#c9c3bb 40%,#8c6a52 70%,#b49a6a 100%)}

/* why choose */
.why{left:0;top:461px;width:1193px;height:280px;background:var(--red)}
.why h2{position:absolute;left:68px;top:24px;font-family:"Oswald",sans-serif;font-weight:500;font-size:23px;color:#fff;letter-spacing:-.3px}
.step{position:absolute;top:70px;width:220px;height:175px;overflow:visible}
.step svg{position:absolute;left:0;top:0;overflow:visible}
.step .label{position:absolute;left:12px;top:75px;width:102px;height:60px;display:flex;align-items:center;justify-content:center;text-align:center;font-family:"Roboto",sans-serif;font-weight:500;font-size:14px;line-height:15px;color:#fff}
.step .num{position:absolute;left:148px;top:16px;width:40px;text-align:center;font-family:"Oswald",sans-serif;font-size:19px;color:#fff}

/* section titles */
.sec-title{font-family:"Oswald",sans-serif;font-weight:500;font-size:23px;color:#444;letter-spacing:-.3px}
.sec-rule{height:1px;background:#bbb}
.sec-rule::before{content:"";position:absolute;left:0;top:-3px;width:84px;height:4px;background:var(--red)}

/* accordion */
.acc-row{position:absolute;height:43px;background:var(--row);display:flex;align-items:center;justify-content:space-between;padding:0 12px 0 16px;font-family:"Oswald",sans-serif;font-size:15px;color:#555;text-transform:uppercase;letter-spacing:-.2px}
.acc-row .plus{position:relative;width:14px;height:14px}
.acc-row .plus::before,.acc-row .plus::after{content:"";position:absolute;background:#777}
.acc-row .plus::before{left:0;top:6px;width:14px;height:2px}
.acc-row .plus::after{left:6px;top:0;width:2px;height:14px}
.acc-row.open{background:var(--red-dark);color:#fff}
.acc-row.open .plus::before{background:#fff}
.acc-row.open .plus::after{display:none}
.acc-panel{left:68px;top:1006px;width:324px;height:129px;background:var(--panel)}
.acc-panel li{list-style:none;position:absolute;left:14px;font-family:"Oswald",sans-serif;font-size:14.5px;color:#555;text-transform:uppercase;display:flex;align-items:center;gap:10px}
.acc-panel li::before{content:"";width:6px;height:6px;background:var(--red)}

/* about */
.about-img{left:800px;top:866px;width:322px;height:201px;background:linear-gradient(135deg,#f4f4f4 0%,#e9e2e2 50%,#d9c8c8 100%)}
.about-text{left:800px;top:1083px;width:322px;font-family:"Open Sans",sans-serif;font-size:12.2px;line-height:15.5px;color:#666}
.about-text a{color:var(--red);text-decoration:none;margin-left:8px}

/* footer */
.foot-rule{left:0;top:1159px;width:1193px;height:3px;background:var(--red-dark)}
.foot-links{left:68px;top:1180px;display:flex;align-items:center;font-family:"Oswald",sans-serif;font-size:14.5px;color:#666}
.foot-links a{color:#666;text-decoration:none;padding:0 9px;border-right:1px solid var(--red);line-height:18px}
.foot-links a:first-child{padding-left:0}
.copy{display:flex;align-items:center;gap:10px;padding-left:9px;font-family:"Roboto",sans-serif;font-weight:700;font-size:11px;color:#555}
.copy i{display:block;width:14px;height:14px;border:1.5px solid var(--red);border-radius:50%}
.copy b{font-weight:700;color:#444}
.badge{left:935px;top:1171px;width:190px;height:32px;background:var(--red-dark);border-radius:10px 10px 0 0;border:2px solid #ddd;border-bottom:none;color:#fff;text-align:right;padding:2px 12px 0 0;font-family:"Roboto",sans-serif;font-size:9.5px;line-height:11.5px}
.badge em{font-weight:700}
</style>
</head>
<body>
<div class="page">

  <header>
    <div class="abs brand"><span class="brand-mark"></span><span class="brand-name">Lunvale Placements</span></div>
    <div class="abs nav-home"></div>
    <nav class="nav">
      <a style="left:428px;top:47px">Home</a>
      <a style="left:500px">Who we are</a>
      <a style="left:592px">Our Approach</a>
      <a style="left:689px">What we do</a>
      <a style="left:776px">Migration Assistance</a>
      <a style="left:912px">Job Seeker</a>
      <a style="left:1000px">Support</a>
      <a style="left:1064px">Contact Us</a>
    </nav>
    <div class="abs header-rule"></div>
  </header>

  <div class="abs band">
    <div class="abs social" aria-label="Social links"><span></span><span></span><span></span><span></span></div>
  </div>

  <div class="abs hero-map" role="img" aria-label="Map of Australia with arcs linking to the United Kingdom, Middle East, Zimbabwe, Botswana, South Africa, Malaysia, China, Singapore, Philippines and New Zealand"></div>
  <div class="abs hero-photo" role="img" aria-label="Photo of a smiling worker in a yellow hard hat"></div>

  <section class="abs why">
    <h2>WHY CHOOSE US ?</h2>

    <div class="step" style="left:67px">
      <svg width="220" height="175" viewBox="0 0 220 175"><line x1="63" y1="105" x2="168" y2="33" stroke="#fff" stroke-width="14"/><circle cx="63" cy="105" r="63" fill="#fff"/><circle cx="63" cy="105" r="50" fill="var(--red)"/><circle cx="168" cy="33" r="29" fill="#fff"/><circle cx="168" cy="33" r="24" fill="var(--red)"/></svg>
      <div class="label">Work as<br>Team with<br>our Clients</div>
      <div class="num">1</div>
    </div>
    <div class="step" style="left:355px">
      <svg width="220" height="175" viewBox="0 0 220 175"><line x1="63" y1="105" x2="168" y2="33" stroke="#fff" stroke-width="14"/><circle cx="63" cy="105" r="63" fill="#fff"/><circle cx="63" cy="105" r="50" fill="var(--red)"/><circle cx="168" cy="33" r="29" fill="#fff"/><circle cx="168" cy="33" r="24" fill="var(--red)"/></svg>
      <div class="label">custtomize<br>recruitment<br>process</div>
      <div class="num">2</div>
    </div>
    <div class="step" style="left:607px">
      <svg width="220" height="175" viewBox="0 0 220 175"><line x1="63" y1="105" x2="168" y2="33" stroke="#fff" stroke-width="14"/><circle cx="63" cy="105" r="63" fill="#fff"/><circle cx="63" cy="105" r="50" fill="var(--red)"/><circle cx="168" cy="33" r="29" fill="#fff"/><circle cx="168" cy="33" r="24" fill="var(--red)"/></svg>
      <div class="label">Strategic<br>Vision</div>
      <div class="num">3</div>
    </div>
    <div class="step" style="left:906px">
      <svg width="220" height="175" viewBox="0 0 220 175"><line x1="63" y1="105" x2="168" y2="33" stroke="#fff" stroke-width="14"/><circle cx="63" cy="105" r="63" fill="#fff"/><circle cx="63" cy="105" r="50" fill="var(--red)"/><circle cx="168" cy="33" r="29" fill="#fff"/><circle cx="168" cy="33" r="24" fill="var(--red)"/></svg>
      <div class="label">Honest &amp;<br>Corporate<br>Citizens</div>
      <div class="num">4</div>
    </div>
  </section>

  <h2 class="abs sec-title" style="left:70px;top:798px">OUR SPECIALIST AREAS</h2>
  <div class="abs sec-rule" style="left:68px;top:842px;width:324px"></div>

  <div class="acc-row" style="left:68px;top:866px;width:324px">Accounting and Corporate Finance<span class="plus"></span></div>
  <div class="acc-row" style="left:68px;top:913px;width:324px">Construction<span class="plus"></span></div>
  <div class="acc-row open" style="left:68px;top:960px;width:324px">Engineering<span class="plus"></span></div>
  <ul class="abs acc-panel">
    <li style="top:10px">Water and Waste Water</li>
    <li style="top:38px">Civil-Mechanical</li>
    <li style="top:66px">Environmental</li>
    <li style="top:94px">Rail and Signalling</li>
  </ul>

  <div class="acc-row" style="left:422px;top:866px;width:325px">Health and Allied Health<span class="plus"></span></div>
  <div class="acc-row" style="left:422px;top:913px;width:325px">Local Government<span class="plus"></span></div>
  <div class="acc-row" style="left:422px;top:958px;width:325px">Manufacturing<span class="plus"></span></div>
  <div class="acc-row" style="left:422px;top:1004px;width:325px">Mining<span class="plus"></span></div>
  <div class="acc-row" style="left:422px;top:1048px;width:325px">Oil and Gas<span class="plus"></span></div>
  <div class="acc-row" style="left:422px;top:1093px;width:325px">Skill Trades People<span class="plus"></span></div>

  <h2 class="abs sec-title" style="left:800px;top:798px">ABOUT US....</h2>
  <div class="abs sec-rule" style="left:800px;top:842px;width:324px"></div>
  <div class="abs about-img" role="img" aria-label="Red map of Australia surrounded by four photos of industrial, engineering, utility and mining work"></div>
  <p class="abs about-text">We are committed to providing the highest standards of service in Executive Search and Selection and the Provision of Skilled trades people and Allied Health Professionals throughout Asustalia.<a href="#">Read More</a></p>

  <div class="abs foot-rule"></div>
  <footer class="abs foot-links">
    <a href="#">HOME</a><a href="#">CONTACT US</a><a href="#">PRIVACY POLICY</a><a href="#">USEFUL LINKS</a><a href="#">SITEMAP</a>
    <span class="copy"><i></i>copyright <b>Lunvale Partners 2013</b></span>
  </footer>
  <div class="abs badge">Lunvale Partners -<br>We can find "<em>Anyone Anywhere</em>"</div>

</div>
</body>
</html>
```